The Ashen Serpent - Book two of the Varro Chronicles

I would like a book cover design for use in self-publishing with Lantern Press Publishing (Brightmart) a Science Fiction novel that is the second book in a trilogy.

In the first book, "The Fury of Heaven", Varro Maximian, a Roman Centurian, is infused with The Fury of Heaven on the day of the crucifixion which makes him a tragic cursed anti-hero unable to be killed. Two thousand years later he is revived by and falls in love with Anna Lee Hartwell a beautiful archeologist student at Harwick University. They are drawn into a battle against a malevolent Artificial Intelligence named Vector bent on the destruction of humanity. Vector is destroyed but Varro appears to have died from absorbing the energy of a nuclear bomb.

In the second book, The Ashen Serpent, Vector returns seeking revenge and targets Anna Lee Hartwell and her unborn child by kidnapping them. The birth of Ravi, the son of The Fury of Heaven and Anna Lee Hartwell awakens Moru Thekal, The Ashen Serpent, who is foretold in Prophesy to be the destroyer of the world. The power in Varro reawakens and he rescues Anna Lee. He then joins forces with Vector to battle The Ashen Serpent in an attempt to prevent the apocalypse.

Copy of the first book cover is included for reference

I have a subscription to Pixvault and artwork from that source can be used in cover design.

The cover should be focused on The Ashen Serpent, the apocalypse or the final battle between The Ashen Serpent and Varro.

The Prophesy and Moru Thekal (The Ashen Serpent), are inspired by the Zoroastrian end of world writings that were a precursor to the Bible's book of Revelations.

The Ashen Serpent is a shape shifting beast that has multiple forms including that of a Dragon. His human form has a multi-headed dragon tattoo on his chest. He also has an axe wielding warrior Djinn form. The beast can mind control humans, is immensely strong, imperious to most physical attacks but when cut its blood becomes a weapon morphing into poison, acid, pestilence or stinging vermin.

I like the photo in Pixvault 418203957 which I feel could work well as the front cover. I also like the concept in Pixvault 2063519408 but do not like the artwork.

Target Market(s)

Adult male and female Science Fiction/Fantasy readers.

Industry/Entity Type

Science Fiction/Fantasy book

Requirements
Must have
• Dramatic art
Nice to have
• Potential concepts for cover: Focus on Ashen Serpent character, focus on climatic battle between Ashen Serpent and Varro, fire, apocalyptic effect of final battle, The rear cover can be continuation of front or can focus on Varro, Anna Lee Hartwell, Ravi (the child) or the apocalypse.
Should not have
• comic art

```html
<!DOCTYPE html>
<html lang="en">
<head>
<meta charset="utf-8">
<title>The Ashen Serpent – Book Two of the Varro Chronicles – Cover Spread</title>
<link rel="stylesheet" href="https://fonts.googleapis.com/css2?family=Black+Ops+One&family=Questrial&display=swap">
<style>
  :root {
    --page: #e6e6e6;
    --ink-black: #000000;
    --ember-deep: #3a0d02;
    --ember: #b8410c;
    --flame: #f08a1e;
    --flare: #ffe2a0;
    --planet-light: #e9a060;
    --planet: #b8632a;
    --planet-dark: #6e2a0a;
    --blood-light: #e0524a;
    --blood: #a3201b;
    --blood-dark: #4a0806;
    --steel-light: #d8d8d8;
    --steel: #7a7a7a;
    --steel-dark: #1e1e1e;
    --paper: #ffffff;
    --text-light: #ffffff;
  }
  * { margin: 0; padding: 0; box-sizing: border-box; }
  html, body {
    width: 1200px; height: 934px; overflow: hidden;
    background: var(--page);
  }
  .spread {
    position: absolute; left: 43px; top: 57px;
    width: 1114px; height: 821px;
    background: var(--ink-black);
    overflow: hidden;
  }

  /* back cover */
  .back-art {
    position: absolute; left: 0; top: 0; width: 467px; height: 821px;
    background:
      radial-gradient(ellipse 230px 200px at 450px 660px, rgba(240,138,30,.8), rgba(184,65,12,.35) 55%, transparent 80%),
      radial-gradient(ellipse 200px 320px at 380px 220px, rgba(130,45,10,.6), transparent 75%),
      radial-gradient(ellipse 140px 110px at 210px 640px, rgba(190,160,60,.3), transparent 80%),
      linear-gradient(90deg, var(--ink-black) 30%, #1c0602 70%, var(--ember-deep) 100%);
  }
  .blurb {
    position: absolute; left: 36px; top: 208px; width: 398px;
    font-family: "Questrial", sans-serif; font-weight: 400;
    font-size: 18px; line-height: 34px;
    color: var(--text-light); text-align: justify;
  }
  .barcode-space {
    position: absolute; left: 197px; top: 659px; width: 243px; height: 134px;
    background: linear-gradient(90deg, var(--paper) 86%, #c8c8c8);
  }

  /* spine */
  .spine-art {
    position: absolute; left: 467px; top: 0; width: 93px; height: 821px;
    background:
      radial-gradient(ellipse 60px 260px at 46px 560px, rgba(240,140,50,.55), transparent 80%),
      linear-gradient(180deg, #1c0602 0%, #5a1c06 35%, #a84a16 68%, #1c0602 100%);
    border-left: 2px solid rgba(255,170,80,.5);
    border-right: 2px solid rgba(255,170,80,.5);
  }

  /* front cover */
  .front-art {
    position: absolute; left: 560px; top: 0; width: 554px; height: 821px;
    overflow: hidden;
    background:
      radial-gradient(ellipse 360px 260px at 276px 330px, var(--flare) 0%, var(--flame) 28%, var(--ember) 58%, var(--ember-deep) 92%),
      var(--ember-deep);
  }
  .flare-rays {
    position: absolute; inset: 0;
    background: repeating-conic-gradient(from 0deg at 276px 372px,
      rgba(255,220,150,.0) 0deg, rgba(255,200,120,.35) 3deg, rgba(255,220,150,0) 7deg,
      rgba(255,150,60,.18) 11deg, rgba(255,220,150,0) 16deg);
    -webkit-mask-image: radial-gradient(circle 520px at 276px 372px, #000 30%, transparent 90%);
            mask-image: radial-gradient(circle 520px at 276px 372px, #000 30%, transparent 90%);
    mix-blend-mode: screen;
  }
  .horizon-flash {
    position: absolute; left: -60px; top: 300px; width: 674px; height: 150px;
    background: radial-gradient(ellipse 340px 60px at 50% 50%, rgba(255,240,200,.95), rgba(255,170,60,.6) 40%, transparent 75%);
  }
  .planet {
    position: absolute; left: 34px; top: 372px; width: 484px; height: 484px;
    border-radius: 50%;
    background: radial-gradient(circle at 50% 30%, var(--planet-light) 0%, var(--planet) 45%, var(--planet-dark) 90%);
    box-shadow: 0 -4px 14px rgba(255,230,170,.95), 0 -10px 50px rgba(255,160,60,.8);
  }
  .hero-figure {
    position: absolute; left: 150px; top: 440px; width: 220px; height: 270px;
    background: radial-gradient(ellipse 90px 130px at 55% 50%, rgba(60,20,8,.85), rgba(90,35,10,.55) 55%, transparent 100%);
  }
  .ground-shadow {
    position: absolute; left: 0; right: 0; bottom: 0; height: 230px;
    background: linear-gradient(180deg, transparent, rgba(20,5,0,.85) 55%, #0d0300);
  }

  .titles { position: absolute; left: 0; top: 0; }
</style>
</head>
<body>
<main class="spread">
  <div class="back-art" role="img" aria-label="Dark smoky background with fire glow rising from the lower right"></div>
  <div class="spine-art" role="img" aria-label="Fiery orange glow running down the spine"></div>

  <div class="front-art" role="img" aria-label="Fiery cosmic explosion bursting over the horizon of a burning planet">
    <div class="flare-rays"></div>
    <div class="horizon-flash"></div>
    <div class="planet"></div>
    <div class="hero-figure" role="img" aria-label="Lone armoured warrior seen from behind, holding a spear and shield"></div>
    <div class="ground-shadow"></div>
  </div>

  <p class="blurb">In the second book, The Ashen Serpent, Vector returns seeking revenge and targets Anna Lee Hartwell and her unborn child by kidnapping them. The birth of Ravi, the son of the Fury of Heaven and Anna Lee Hartwell awakens Moru Thekal, the Ashen Serpent, who is foretold in Prophesy to be the destroyer of the world. The power in Varro reawakens and he rescues Anna Lee. He then joins forces with Vector to battle the Ashen Serpent in an attempt to prevent the apocalypse.</p>

  <div class="barcode-space"></div>

  <svg class="titles" width="1114" height="821" viewBox="0 0 1114 821">
    <defs>
      <linearGradient id="blood-fill" x1="0" y1="0" x2="0" y2="1">
        <stop offset="0" stop-color="var(--blood-light)"/>
        <stop offset=".55" stop-color="var(--blood)"/>
        <stop offset="1" stop-color="var(--blood-dark)"/>
      </linearGradient>
      <linearGradient id="steel-fill" x1="0" y1="0" x2="0" y2="1">
        <stop offset="0" stop-color="var(--steel-light)"/>
        <stop offset=".5" stop-color="var(--steel)"/>
        <stop offset="1" stop-color="var(--steel-dark)"/>
      </linearGradient>
      <linearGradient id="blood-fill-h" x1="0" y1="0" x2="1" y2="0">
        <stop offset="0" stop-color="var(--blood-light)"/>
        <stop offset=".55" stop-color="var(--blood)"/>
        <stop offset="1" stop-color="var(--blood-dark)"/>
      </linearGradient>
      <linearGradient id="steel-fill-h" x1="0" y1="0" x2="1" y2="0">
        <stop offset="0" stop-color="var(--steel-light)"/>
        <stop offset=".5" stop-color="var(--steel)"/>
        <stop offset="1" stop-color="var(--steel-dark)"/>
      </linearGradient>
    </defs>

    <g class="back-title" font-family="'Black Ops One', sans-serif" text-anchor="middle">
      <text x="236" y="57" font-family="'Questrial', sans-serif" font-size="22" fill="var(--text-light)">THE</text>
      <text x="236" y="141" font-size="100" textLength="214" lengthAdjust="spacingAndGlyphs" fill="url(#blood-fill)" stroke="var(--blood-dark)" stroke-width="1">ASHEN</text>
      <text x="236" y="186" font-size="52" textLength="214" lengthAdjust="spacingAndGlyphs" fill="url(#steel-fill)" stroke="#111" stroke-width="1">SERPENT</text>
    </g>

    <g class="spine-text" font-family="'Black Ops One', sans-serif">
      <text transform="translate(527,800) rotate(-90)" font-family="'Questrial', sans-serif" font-size="24" textLength="178" lengthAdjust="spacingAndGlyphs" fill="var(--text-light)">CALDER WRENFIELD</text>
      <text transform="translate(527,578) rotate(-90)" font-family="'Questrial', sans-serif" font-size="30" textLength="55" lengthAdjust="spacingAndGlyphs" fill="var(--text-light)">THE</text>
      <text transform="translate(536,501) rotate(-90)" font-size="66" textLength="160" lengthAdjust="spacingAndGlyphs" fill="url(#blood-fill-h)" stroke="var(--blood-dark)" stroke-width="1">ASHEN</text>
      <text transform="translate(536,330) rotate(-90)" font-size="66" textLength="310" lengthAdjust="spacingAndGlyphs" fill="url(#steel-fill-h)" stroke="#111" stroke-width="1">SERPENT</text>
    </g>

    <g class="front-title" font-family="'Black Ops One', sans-serif" text-anchor="middle">
      <text x="836" y="91" font-family="'Questrial', sans-serif" font-size="46" fill="var(--text-light)">THE</text>
      <text x="835" y="267" font-size="190" textLength="420" lengthAdjust="spacingAndGlyphs" fill="url(#blood-fill)" stroke="var(--blood-dark)" stroke-width="2">ASHEN</text>
      <text x="835" y="358" font-size="100" textLength="420" lengthAdjust="spacingAndGlyphs" fill="url(#steel-fill)" stroke="#111" stroke-width="1.5">SERPENT</text>
    </g>

    <g class="front-credits" font-family="'Questrial', sans-serif" fill="var(--text-light)" text-anchor="middle">
      <text x="834" y="731" font-size="24" textLength="358" lengthAdjust="spacingAndGlyphs">BOOK TWO - THE VARRO CHRONICLES</text>
      <text x="834" y="786" font-size="48" textLength="361" lengthAdjust="spacingAndGlyphs">CALDER WRENFIELD</text>
    </g>
  </svg>
</main>
</body>
</html>
```